Flyer for Aluminium recycling business

We are a startup aluminium recycling business. We don’t have a logo yet. I’ve attached a flyer created by one of our sales people but it’s a bit average and we need something a bit more modern and slick. You have creative license to completely change everything - as long as the information being communicated is the same.

Target Market(s)

Hospitality, Hotels, Apartment blocks, malls etcs

Industry/Entity Type

Aluminium recycling

Requirements
Must have
• the wording
Nice to have
• you have free license on design aspect

```html
<!DOCTYPE html>
<html lang="en">
<head>
<meta charset="utf-8">
<title>Brightloop Metals – Aluminium Recycling Flyer</title>
<link href="https://fonts.googleapis.com/css2?family=Outfit:wght@400;500;600;700;800&display=swap" rel="stylesheet">
<style>
  :root {
    --stage: #a9a89c;
    --yellow: #f1c940;
    --yellow-deep: #e9bd2f;
    --mint-top: #dff5d8;
    --mint-bottom: #f1fbec;
    --forest: #0d3a24;
    --ink: #1c140f;
    --green: #3fae3f;
    --green-dark: #2f8f2f;
    --leaf: #6da93a;
    --brown: #4b2c20;
    --bar: #4f9212;
    --gold: #f4cd2e;
    --white: #ffffff;
  }
  * { box-sizing: border-box; margin: 0; padding: 0; }
  html, body { width: 916px; height: 1200px; overflow: hidden; }
  body {
    background: var(--stage);
    font-family: "Outfit", sans-serif;
    color: var(--ink);
    position: relative;
  }
  .flyer {
    position: absolute;
    left: 34px; top: 0;
    width: 848px; height: 1200px;
    background: linear-gradient(180deg, var(--mint-top), var(--mint-bottom));
    overflow: hidden;
  }
  .hero {
    position: absolute; left: 0; top: 0;
    width: 848px; height: 511px;
    background: radial-gradient(ellipse at center, var(--yellow) 40%, var(--yellow-deep) 100%);
  }
  .brand {
    position: absolute; left: 0; width: 100%; top: 190px;
    display: flex; align-items: center; justify-content: center; gap: 16px;
  }
  .brand-mark {
    width: 62px; height: 62px; border-radius: 50%;
    background: var(--forest);
  }
  .brand-name {
    font-weight: 800; font-size: 52px; line-height: 1;
    color: var(--forest); letter-spacing: -0.5px;
  }
  .tagline {
    position: absolute; left: 0; width: 100%; top: 306px;
    text-align: center; font-size: 20px; font-weight: 500;
    line-height: 25px; color: var(--ink);
  }
  .cycle { position: absolute; left: 0; top: 511px; }
  .partnership {
    position: absolute; left: 41px; top: 640px; width: 180px;
    font-size: 17px; font-weight: 700; line-height: 19px;
    text-transform: uppercase; color: var(--ink);
  }
  .here {
    position: absolute; left: 325px; width: 200px; top: 662px;
    text-align: center; font-weight: 700; color: var(--ink);
  }
  .here-small { display: block; font-size: 27px; line-height: 28px; }
  .here-big { display: block; font-size: 44px; line-height: 44px; }
  .col { position: absolute; top: 862px; }
  .col-simple { left: 41px; width: 410px; }
  .col-take { left: 490px; width: 330px; }
  .col h2 {
    font-size: 18px; font-weight: 700; text-transform: uppercase;
    margin-bottom: 14px; letter-spacing: 0.1px;
  }
  .checklist { list-style: none; }
  .checklist li {
    position: relative; padding-left: 34px;
    font-size: 14.5px; line-height: 17px; margin-bottom: 14px;
  }
  .checklist svg { position: absolute; left: 0; top: 0; width: 17px; height: 17px; }
  .contact-bar {
    position: absolute; left: 0; top: 1141px;
    width: 848px; height: 59px; background: var(--bar);
    display: flex; align-items: center; justify-content: center; gap: 58px;
    color: var(--white);
  }
  .contact { display: flex; align-items: center; gap: 16px; }
  .contact-phone { font-size: 30px; font-weight: 600; }
  .contact-email { font-size: 21px; font-weight: 500; }
</style>
</head>
<body>
<main class="flyer">
  <section class="hero" role="img" aria-label="Photograph of crushed coloured drink cans, foil, a foil tray and bottle caps on a yellow surface"></section>

  <div class="brand">
    <span class="brand-mark"></span>
    <span class="brand-name">BRIGHTLOOP METALS</span>
  </div>
  <p class="tagline">PLAYING THE FAIR ALUMINUM RECYCLING GAME<br>FOR GOOD</p>

  <svg class="cycle" width="848" height="360" viewBox="0 511 848 360" aria-hidden="true">
    <circle cx="423" cy="703" r="143" fill="none" stroke="#5a3a28" stroke-width="1.5" stroke-dasharray="5 4"/>
    <!-- recycle -->
    <circle cx="423" cy="557" r="26" fill="var(--green)"/>
    <path d="M423 546 L434 565 L412 565 Z" fill="none" stroke="#fff" stroke-width="3" stroke-linejoin="round"/>
    <!-- bin -->
    <circle cx="531" cy="610" r="26" fill="var(--leaf)"/>
    <path d="M521 601 h20 M523 604 h16 l-2 18 h-12 Z" fill="#fff" stroke="#fff" stroke-width="2" stroke-linejoin="round"/>
    <!-- can -->
    <circle cx="560" cy="702" r="26" fill="var(--green-dark)"/>
    <rect x="552" y="690" width="16" height="24" rx="3" fill="#d5d9d6"/>
    <!-- truck -->
    <circle cx="513" cy="803" r="26" fill="var(--leaf)"/>
    <rect x="505" y="794" width="20" height="14" fill="#fff"/>
    <path d="M505 798 h-7 l-4 5 v5 h11 Z" fill="#fff"/>
    <circle cx="500" cy="811" r="3" fill="#444"/><circle cx="519" cy="811" r="3" fill="#444"/>
    <!-- factory -->
    <circle cx="419" cy="840" r="26" fill="var(--green)"/>
    <path d="M405 852 v-12 l8 -5 v5 l8 -5 v17 Z" fill="var(--gold)"/>
    <rect x="423" y="828" width="4" height="24" fill="#fff"/><rect x="429" y="832" width="4" height="20" fill="#fff"/>
    <!-- ingot -->
    <circle cx="321" cy="797" r="26" fill="var(--brown)"/>
    <rect x="312" y="786" width="18" height="22" fill="#d9d9d9"/>
    <path d="M315 786 v22 M319 786 v22 M323 786 v22 M327 786 v22" stroke="#888" stroke-width="1"/>
    <!-- cycle -->
    <circle cx="288" cy="708" r="26" fill="var(--leaf)"/>
    <circle cx="288" cy="708" r="13" fill="none" stroke="#fff" stroke-width="2.5"/>
    <circle cx="288" cy="708" r="5" fill="#fff"/>
    <!-- payment -->
    <circle cx="310" cy="613" r="26" fill="var(--brown)"/>
    <rect x="300" y="604" width="20" height="13" rx="2" fill="var(--green)" transform="rotate(-20 310 610)"/>
    <rect x="296" y="614" width="10" height="8" fill="#fff"/>
  </svg>

  <p class="partnership">Our partnership with you is based on common sense, mutual gain and a better tomorrow</p>

  <div class="here">
    <span class="here-small">YOU ARE</span>
    <span class="here-big">HERE</span>
  </div>

  <section class="col col-simple">
    <h2>It’s simple</h2>
    <ul class="checklist">
      <li><svg viewBox="0 0 17 17"><path d="M14 8v7H1V2h9" fill="none" stroke="#1c140f" stroke-width="1.8"/><path d="M4 7l4 4 8-9" fill="none" stroke="#1c140f" stroke-width="2.2"/></svg>We bring you a free bin</li>
      <li><svg viewBox="0 0 17 17"><path d="M14 8v7H1V2h9" fill="none" stroke="#1c140f" stroke-width="1.8"/><path d="M4 7l4 4 8-9" fill="none" stroke="#1c140f" stroke-width="2.2"/></svg>You throw all and any aluminium waste into<br>the bin - no need te super-clean it. Try to compact /<br>squash the aluminium as much possible, and<br>take off lids tear.</li>
      <li><svg viewBox="0 0 17 17"><path d="M14 8v7H1V2h9" fill="none" stroke="#1c140f" stroke-width="1.8"/><path d="M4 7l4 4 8-9" fill="none" stroke="#1c140f" stroke-width="2.2"/></svg>We collect the bin at no charge</li>
      <li><svg viewBox="0 0 17 17"><path d="M14 8v7H1V2h9" fill="none" stroke="#1c140f" stroke-width="1.8"/><path d="M4 7l4 4 8-9" fill="none" stroke="#1c140f" stroke-width="2.2"/></svg>We turn the aluminium waste into a desirable resource</li>
      <li><svg viewBox="0 0 17 17"><path d="M14 8v7H1V2h9" fill="none" stroke="#1c140f" stroke-width="1.8"/><path d="M4 7l4 4 8-9" fill="none" stroke="#1c140f" stroke-width="2.2"/></svg>We pay you for however much of that resource<br>your waste has generated - and give you a report on<br>that, so you can see how good you are</li>
    </ul>
  </section>

  <section class="col col-take">
    <h2>Examples of what we can take</h2>
    <ul class="checklist">
      <li><svg viewBox="0 0 17 17"><path d="M14 8v7H1V2h9" fill="none" stroke="#1c140f" stroke-width="1.8"/><path d="M4 7l4 4 8-9" fill="none" stroke="#1c140f" stroke-width="2.2"/></svg>Used beverage cans - any</li>
      <li><svg viewBox="0 0 17 17"><path d="M14 8v7H1V2h9" fill="none" stroke="#1c140f" stroke-width="1.8"/><path d="M4 7l4 4 8-9" fill="none" stroke="#1c140f" stroke-width="2.2"/></svg>Tinfoil - scrunched, crusty, burned or dirty</li>
      <li><svg viewBox="0 0 17 17"><path d="M14 8v7H1V2h9" fill="none" stroke="#1c140f" stroke-width="1.8"/><path d="M4 7l4 4 8-9" fill="none" stroke="#1c140f" stroke-width="2.2"/></svg>Disposable BBQ roasting trays</li>
      <li><svg viewBox="0 0 17 17"><path d="M14 8v7H1V2h9" fill="none" stroke="#1c140f" stroke-width="1.8"/><path d="M4 7l4 4 8-9" fill="none" stroke="#1c140f" stroke-width="2.2"/></svg>Aluminium takeaway containers</li>
      <li><svg viewBox="0 0 17 17"><path d="M14 8v7H1V2h9" fill="none" stroke="#1c140f" stroke-width="1.8"/><path d="M4 7l4 4 8-9" fill="none" stroke="#1c140f" stroke-width="2.2"/></svg>Wine bottle screw tops (and collars - if<br>you can get them off)</li>
      <li><svg viewBox="0 0 17 17"><path d="M14 8v7H1V2h9" fill="none" stroke="#1c140f" stroke-width="1.8"/><path d="M4 7l4 4 8-9" fill="none" stroke="#1c140f" stroke-width="2.2"/></svg>Tear-off can lids</li>
    </ul>
  </section>

  <footer class="contact-bar">
    <div class="contact">
      <svg width="26" height="26" viewBox="0 0 24 24" aria-hidden="true"><path d="M6.6 10.8a15 15 0 0 0 6.6 6.6l2.2-2.2a1 1 0 0 1 1-.25 11.4 11.4 0 0 0 3.6.6 1 1 0 0 1 1 1V20a1 1 0 0 1-1 1A17 17 0 0 1 3 4a1 1 0 0 1 1-1h3.5a1 1 0 0 1 1 1c0 1.25.2 2.45.6 3.6a1 1 0 0 1-.25 1Z" fill="var(--gold)"/></svg>
      <span class="contact-phone">021 555 0178</span>
    </div>
    <div class="contact">
      <svg width="28" height="20" viewBox="0 0 28 20" aria-hidden="true"><rect x="1" y="1" width="26" height="18" fill="none" stroke="var(--gold)" stroke-width="2"/><path d="M1 1l13 10L27 1M1 19l10-9M27 19l-10-9" fill="none" stroke="var(--gold)" stroke-width="2"/></svg>
      <span class="contact-email">join@brightloopmetals.co.nz</span>
    </div>
  </footer>
</main>
</body>
</html>
```